Mara Lindqvist Advisory Business Cards

Hi - using the information and logo provided I require a two sided business card designed with the following information. The business card is a 'mini card' 3.5" x 1.25".

Front of card should be the logo attached but inverted (so the background is the peach colour and the logo white).

Back should have these details. If we can't fit the Instragram and Facebook part can we just put the little logos.

Mara Lindqvist

Art and Design Consultant
Dealer - Curator - Events - Styling - Creative Sourcing

P: 0438 519 207
E: mara@maralindqvistadvisory.com
W: www.maralindqvistadvisory.com
I (instagram image please): maralindqvistadvisory F (Facebook image please): MaraLindqvistAdvisor

Target Market(s)

Galleries, artists, art buyers, interior design clients, event managers, creative types

Industry/Entity Type

Business

```html
<!DOCTYPE html>
<html lang="en">
<head>
<meta charset="utf-8">
<title>Mara Lindqvist Advisory – Mini Business Card</title>
<link href="https://fonts.googleapis.com/css2?family=Tinos:wght@400&family=Arimo:wght@700&display=swap" rel="stylesheet">
<style>
  :root {
    --peach: #f3b89c;
    --peach-light: #f7cbb6;
    --ink: #6e6e6e;
    --label: #000000;
    --paper: #ffffff;
  }
  html, body {
    margin: 0;
    padding: 0;
    width: 1171px;
    height: 1200px;
    overflow: hidden;
    background: var(--paper);
  }
  .sheet {
    position: relative;
    width: 1171px;
    height: 1200px;
    overflow: hidden;
    font-family: "Tinos", "Times New Roman", serif;
    color: var(--ink);
  }
  .side-label {
    position: absolute;
    margin: 0;
    font-family: "Arimo", Arial, sans-serif;
    font-weight: 700;
    font-size: 42px;
    color: var(--label);
    line-height: 1;
  }
  .side-label--front { left: 115px; top: 68px; }
  .side-label--back  { left: 119px; top: 648px; }

  /* Front */
  .card-front {
    position: absolute;
    left: 105px;
    top: 156px;
    width: 930px;
    height: 324px;
    background: var(--peach);
  }
  .brand-dot {
    position: absolute;
    border-radius: 50%;
  }
  .card-front .brand-dot {
    left: 255px;
    top: 31px;
    width: 116px;
    height: 116px;
    background: var(--paper);
  }
  .wordmark {
    position: absolute;
    margin: 0;
    text-align: center;
    font-weight: 400;
    color: var(--ink);
    white-space: nowrap;
    line-height: 1;
  }
  .card-front .wordmark--name {
    left: 60px;
    width: 506px;
    top: 214px;
    font-size: 44px;
    letter-spacing: 0.16em;
    padding-left: 0.16em;
  }
  .card-front .wordmark--tag {
    left: 60px;
    width: 506px;
    top: 278px;
    font-size: 24px;
    letter-spacing: 0.5em;
    padding-left: 0.5em;
  }

  /* Back */
  .card-back {
    position: absolute;
    left: 105px;
    top: 700px;
    width: 930px;
    height: 340px;
  }
  .contact-line {
    position: absolute;
    left: 30px;
    margin: 0;
    font-size: 24px;
    line-height: 1;
    white-space: nowrap;
  }
  .contact-line--phone { top: 128px; letter-spacing: 0.08em; }
  .contact-line--email { top: 164px; }
  .social-line {
    position: absolute;
    left: 30px;
    display: flex;
    align-items: center;
    gap: 10px;
    font-size: 24px;
    line-height: 1;
    white-space: nowrap;
  }
  .social-line--first  { top: 243px; }
  .social-line--second { top: 279px; }
  .social-mark {
    width: 30px;
    height: 30px;
    border-radius: 5px;
    background: var(--peach);
    flex: none;
  }
  .card-back .brand-dot {
    left: 694px;
    top: 26px;
    width: 120px;
    height: 120px;
    background: var(--peach);
  }
  .card-back .wordmark--name {
    left: 580px;
    width: 348px;
    top: 164px;
    font-size: 30px;
    letter-spacing: 0.16em;
    padding-left: 0.16em;
  }
  .card-back .wordmark--tag {
    left: 580px;
    width: 348px;
    top: 204px;
    font-size: 17px;
    letter-spacing: 0.5em;
    padding-left: 0.5em;
  }
  .website {
    position: absolute;
    left: 560px;
    width: 380px;
    top: 281px;
    margin: 0;
    text-align: center;
    font-size: 24px;
    line-height: 1;
    white-space: nowrap;
  }
</style>
</head>
<body>
<main class="sheet">
  <h2 class="side-label side-label--front">Front:</h2>
  <section class="card-front" aria-label="Card front">
    <span class="brand-dot" aria-hidden="true"></span>
    <p class="wordmark wordmark--name">MARA LINDQVIST</p>
    <p class="wordmark wordmark--tag">ADVISORY</p>
  </section>

  <h2 class="side-label side-label--back">Back:</h2>
  <section class="card-back" aria-label="Card back">
    <p class="contact-line contact-line--phone">Mobile: 0438 519 207</p>
    <p class="contact-line contact-line--email">Email: mara@maralindqvistadvisory.com</p>
    <div class="social-line social-line--first">
      <span class="social-mark" aria-hidden="true"></span>
      <span>maralindqvistadvisory</span>
    </div>
    <div class="social-line social-line--second">
      <span class="social-mark" aria-hidden="true"></span>
      <span>MaraLindqvistAdvisor</span>
    </div>

    <span class="brand-dot" aria-hidden="true"></span>
    <p class="wordmark wordmark--name">MARA LINDQVIST</p>
    <p class="wordmark wordmark--tag">ADVISORY</p>
    <p class="website">www.maralindqvistadvisory.com</p>
  </section>
</main>
</body>
</html>
```